Need Business Card Design, Letterhead and a Basic Form layout based on Existing Logo

We need (1) a business card design, (2) a letterhead design and (3) a basic form layout for an international holding company. This holding company has just formed two (2) sub-companies. The logo is the same for each company with only a simple word change for each company. The business card, letterhead and form design will be essentially the same for each company... with only the one word change being different.
The names of the companies are as follows:
1. Halvorn Trust Services
2. Halvorn Immigration Services
The design for the business card, letterhead and Form must be strong, clean and classy.
Our clients will be older, wealthy and mostly Asian. The design must project strength, stability and confidence.
The card may contain the following data:
1. The Logo
2. The name of the person
3. The title of the person
4. The address of the company
5. The Company Phone number
6. The personal mobile number
7. The Skype number (VOIP)
8. The WICKR number (IM)
9. The email
10. The website
We will attach AI files of our logo for the "Halvorn Trust Services" company in the colors Black/White and Blue in both Horizontal and Vertical format... We have also included separate files of the logo icon.
We uploaded the AI files to give the designer the maximum options regarding color and effects. We included the separate files for the icon because we would like to give the designer the option of a watermark. Also, we think it might be nice to highlight the icon on the back of the card perhaps with the website address.
We are not sure which colors or color combinations would be best for these two companies. We know the colors must again project strength, stability and confidence. Perhaps, a combination that might include Tan, Black and White... not sure... need design help... remember this has to have the presence of a bank-like institution... no cartoonish designs or flashy color combinations... please.
The basic form layout will be used for various questionaires, input sheets and instructions.... etc.
NOTE: The fonts used in the logo are Trajan Pro Bold for word "HALVORN" and Trajan Pro Regular for "XXXXXXXXX SERVICES".

```html
<!DOCTYPE html>
<html lang="en">
<head>
<meta charset="utf-8">
<title>Halvorn Trust Services – Stationery</title>
<link rel="stylesheet" href="https://fonts.googleapis.com/css2?family=Cinzel:wght@400;700&display=swap">
<style>
  :root {
    --ink: #141414;
    --red: #c4161c;
    --paper: #ffffff;
    --stage: #e9e7e4;
    --faint: #ececec;
    --band-text: #d9d9d9;
  }
  * { box-sizing: border-box; margin: 0; padding: 0; }
  html, body { width: 1200px; height: 900px; overflow: hidden; }
  body {
    background: var(--stage);
    font-family: "Cinzel", "Times New Roman", serif;
    color: var(--ink);
    position: relative;
  }

  /* ---------- Letterhead ---------- */
  .letterhead {
    position: absolute; left: 90px; top: 90px;
    width: 500px; height: 707px;
    background: var(--paper);
    box-shadow: 0 6px 18px rgba(0,0,0,.18);
    overflow: hidden;
  }
  .brand { display: flex; flex-direction: column; align-items: center; }
  .brand-mark { width: 22px; height: 22px; background: var(--ink); margin-bottom: 8px; }
  .brand-name { font-weight: 700; color: var(--ink); text-align: center; line-height: 1.15; letter-spacing: .04em; }
  .letterhead .brand { position: absolute; top: 42px; left: 0; right: 0; }
  .letterhead .brand-name { font-size: 19px; }
  .letterhead .brand-name span { display: block; font-size: 11px; letter-spacing: .06em; }

  .watermark {
    position: absolute; left: 0; right: 0; top: 410px;
    text-align: center; font-weight: 700; font-size: 66px;
    color: var(--faint); letter-spacing: .05em;
  }

  .letterhead-footer {
    position: absolute; left: 0; right: 0; bottom: 0; height: 56px;
    background: var(--ink); display: flex; align-items: center;
    font-size: 8px; color: var(--band-text); letter-spacing: .04em;
  }
  .footer-item { display: flex; align-items: center; gap: 6px; padding-left: 28px; }
  .footer-item + .footer-item { padding-left: 70px; }
  .footer-address {
    margin-left: auto; height: 100%; width: 158px;
    background: var(--red); color: #fff;
    display: flex; align-items: flex-start; gap: 5px;
    padding: 10px 10px; font-size: 7px; line-height: 1.4;
  }
  .icon { width: 9px; height: 9px; flex: none; fill: currentColor; }

  /* ---------- Business cards ---------- */
  .card {
    position: absolute; width: 420px; height: 240px;
    background: var(--paper);
    box-shadow: 0 6px 18px rgba(0,0,0,.18);
    overflow: hidden;
  }
  .card-front { left: 690px; top: 150px; }
  .card-back  { left: 690px; top: 450px; }

  .card-front .brand { position: absolute; top: 62px; left: 0; right: 0; }
  .card-front .brand-name { font-size: 26px; }
  .card-front .brand-name span { display: block; font-size: 14px; letter-spacing: .06em; }
  .card-front .brand-mark { width: 30px; height: 30px; margin-bottom: 10px; }
  .front-strip {
    position: absolute; left: 0; right: 0; bottom: 0; height: 10px;
    background: var(--ink);
  }
  .front-strip::after {
    content: ""; position: absolute; right: 0; top: 0; bottom: 0; width: 90px;
    background: var(--red);
  }

  .card-back .brand { position: absolute; left: 26px; top: 30px; align-items: flex-start; }
  .card-back .brand-mark { width: 24px; height: 24px; margin-bottom: 8px; }
  .card-back .brand-name { font-size: 15px; text-align: left; }
  .card-back .brand-name span { display: block; font-size: 9px; letter-spacing: .06em; }

  .holder { position: absolute; left: 196px; top: 50px; }
  .holder-name { font-size: 22px; font-weight: 400; letter-spacing: .06em; }
  .holder-title { font-size: 8px; color: var(--red); letter-spacing: .12em; margin-top: 2px; }

  .back-band {
    position: absolute; left: 0; right: 0; bottom: 0; height: 118px;
    background: var(--ink); color: var(--band-text);
    font-size: 7.5px; letter-spacing: .05em; line-height: 1.6;
  }
  .contact-group { position: absolute; display: flex; align-items: center; gap: 8px; }
  .band-tab {
    width: 14px; background: var(--red); color: #fff; flex: none;
    display: flex; flex-direction: column; align-items: center; justify-content: space-evenly;
  }
  .band-tab .icon { width: 8px; height: 8px; }
  .online { left: 236px; top: 12px; }
  .online .band-tab { height: 40px; }
  .phones { left: 26px; top: 44px; }
  .phones .band-tab { height: 28px; }
  .card-address { left: 26px; top: 80px; }
  .card-address .band-tab { height: 26px; }
</style>
</head>
<body>

  <section class="letterhead" aria-label="Letterhead">
    <div class="brand">
      <div class="brand-mark"></div>
      <div class="brand-name">HALVORN<span>TRUST SERVICES</span></div>
    </div>
    <div class="watermark" aria-hidden="true">HALVORN</div>
    <footer class="letterhead-footer">
      <div class="footer-item">
        <svg class="icon" viewBox="0 0 10 10"><path d="M2 0.5 L3.6 2.6 L2.8 3.6 Q4 6 6.4 7.2 L7.4 6.4 L9.5 8 L8.4 9.5 Q1 8.6 0.5 1.6 Z"/></svg>
        <span>502-2190-40-72</span>
      </div>
      <div class="footer-item">
        <svg class="icon" viewBox="0 0 10 10"><path d="M5 0.8 L9.5 5 H8 V9.2 H6 V6.5 H4 V9.2 H2 V5 H0.5 Z"/></svg>
        <span>www.halvorntrust.com</span>
      </div>
      <div class="footer-address">
        <svg class="icon" viewBox="0 0 10 10"><path d="M5 0.3 A3.3 3.3 0 0 1 8.3 3.6 C8.3 6 5 9.7 5 9.7 C5 9.7 1.7 6 1.7 3.6 A3.3 3.3 0 0 1 5 0.3 Z M5 2.3 A1.3 1.3 0 1 0 5 4.9 A1.3 1.3 0 1 0 5 2.3 Z"/></svg>
        <span>Plaza Merida Centre, Office 10, Calle Los Olivos 14, Antigua, Guatemala</span>
      </div>
    </footer>
  </section>

  <section class="card card-front" aria-label="Business card front">
    <div class="brand">
      <div class="brand-mark"></div>
      <div class="brand-name">HALVORN<span>TRUST SERVICES</span></div>
    </div>
    <div class="front-strip"></div>
  </section>

  <section class="card card-back" aria-label="Business card back">
    <div class="brand">
      <div class="brand-mark"></div>
      <div class="brand-name">HALVORN<span>TRUST SERVICES</span></div>
    </div>
    <div class="holder">
      <div class="holder-name">MARCUS DELDEN</div>
      <div class="holder-title">MANAGING DIRECTOR</div>
    </div>
    <div class="back-band">
      <div class="contact-group online">
        <div class="band-tab">
          <svg class="icon" viewBox="0 0 10 10"><circle cx="5" cy="5" r="4.2"/></svg>
          <svg class="icon" viewBox="0 0 10 10"><path d="M0.5 2 H9.5 V8 H0.5 Z M1 2.4 L5 5.6 L9 2.4" stroke="#c4161c" stroke-width=".8"/></svg>
          <svg class="icon" viewBox="0 0 10 10"><path d="M5 0.8 L9.5 5 H8 V9.2 H6 V6.5 H4 V9.2 H2 V5 H0.5 Z"/></svg>
        </div>
        <div>halvorn.direct<br>info@halvorntrust.com<br>www.halvorntrust.com</div>
      </div>
      <div class="contact-group phones">
        <div class="band-tab">
          <svg class="icon" viewBox="0 0 10 10"><path d="M2 0.5 L3.6 2.6 L2.8 3.6 Q4 6 6.4 7.2 L7.4 6.4 L9.5 8 L8.4 9.5 Q1 8.6 0.5 1.6 Z"/></svg>
        </div>
        <div>502-2190-40-72<br>502-5318-27-09</div>
      </div>
      <div class="contact-group card-address">
        <div class="band-tab">
          <svg class="icon" viewBox="0 0 10 10"><path d="M5 0.3 A3.3 3.3 0 0 1 8.3 3.6 C8.3 6 5 9.7 5 9.7 C5 9.7 1.7 6 1.7 3.6 A3.3 3.3 0 0 1 5 0.3 Z"/></svg>
        </div>
        <div>Plaza Merida Centre, Office 10, Calle Los Olivos 14,<br>Antigua, Guatemala</div>
      </div>
    </div>
  </section>

</body>
</html>
```